Very Simple/Minimal Business Card Design Project

The company operates in the industrial maritime infrastructure sector in Brazil. You can find more information on our website www.navelquor.com.br WE NEED TO LOOK POWERFUL AND SERIOUS
I have attached a copy of the old cards. We would like something more professional / industrial / sexy that also includes the position.

The card can be double sided or not. We would like you to propose as many options.

Thank you
Updates

Many thanks, do let me know if you have any questions. I am under a lot of time pressure to try and have them printed over the next days or so.

Please could you use the following information

for the address: Rua Tapiraçu, 418 - Centro, Rio de Janeiro, 20135-070, Brasil

for the mobile: +55 21 8372 9041
for the landline: +55 21 4067 3859

and position:  Diretor Geral

Thakn you

Target Market(s)

Shipowners, bankers, industrial companies

Industry/Entity Type

Industrial

Requirements
Must have
• POWERFUL
SERIOUS
SOLID
BIG CORPORATION

```html
<!DOCTYPE html>
<html lang="pt-BR">
<head>
<meta charset="utf-8">
<title>Navelquor – Cartão de Visita</title>
<link rel="stylesheet" href="https://fonts.googleapis.com/css2?family=Source+Sans+3:ital,wght@0,400;0,600;0,700;1,400&display=swap">
<style>
  :root {
    --navy: #26336e;
    --green: #009e47;
    --white: #ffffff;
    --backdrop: #eceeef;
    --font: "Source Sans 3", sans-serif;
  }
  * { margin: 0; padding: 0; box-sizing: border-box; }
  html, body {
    width: 1200px;
    height: 898px;
    overflow: hidden;
    background: var(--backdrop);
    font-family: var(--font);
  }
  .card {
    position: absolute;
    left: 80px;
    top: 118px;
    width: 1040px;
    height: 662px;
    background: var(--white);
    box-shadow: 0 4px 18px rgba(0, 0, 0, 0.12);
    overflow: hidden;
  }
  .brand {
    position: absolute;
    left: 172px;
    top: 48px;
    height: 136px;
    display: flex;
    align-items: center;
    gap: 20px;
  }
  .brand-mark {
    width: 136px;
    height: 136px;
    border-radius: 12px;
    background: var(--green);
  }
  .brand-name {
    font-size: 96px;
    font-weight: 700;
    color: var(--navy);
    letter-spacing: 2px;
    line-height: 1;
  }
  .divider-band {
    position: absolute;
    left: 0;
    top: 222px;
    width: 100%;
    height: 42px;
    background: var(--navy);
  }
  .contact-panel {
    position: absolute;
    left: 0;
    top: 302px;
    width: 100%;
    height: 360px;
    background: var(--green);
    color: var(--white);
  }
  .person {
    position: absolute;
    left: 0;
    top: 14px;
    width: 100%;
    text-align: center;
  }
  .person-name {
    font-size: 44px;
    font-weight: 600;
    line-height: 48px;
  }
  .person-role {
    font-size: 24px;
    font-weight: 600;
    letter-spacing: 4px;
    text-transform: uppercase;
    line-height: 30px;
  }
  .website {
    font-size: 30px;
    font-style: italic;
    line-height: 36px;
  }
  .details {
    position: absolute;
    top: 170px;
    font-size: 31px;
    line-height: 42px;
    list-style: none;
  }
  .details-address { left: 108px; }
  .details-phone { left: 526px; }
</style>
</head>
<body>
  <main class="card">
    <div class="brand">
      <div class="brand-mark"></div>
      <span class="brand-name">NAVELQUOR</span>
    </div>

    <div class="divider-band"></div>

    <section class="contact-panel">
      <div class="person">
        <p class="person-name">Rafael Monteiro</p>
        <p class="person-role">Diretor Geral</p>
        <p class="website">www.navelquor.com.br</p>
      </div>

      <ul class="details details-address">
        <li>Rua Tapiraçu, 418</li>
        <li>Centro</li>
        <li>CEP 20135-070</li>
        <li>Rio de Janeiro, Brasil</li>
      </ul>

      <ul class="details details-phone">
        <li>T: + 55 21 4067 3859</li>
        <li>M: + 55 21 8372 9041</li>
        <li>rafael@navelquor.com.br</li>
      </ul>
    </section>
  </main>
</body>
</html>
```